Shampoo and Shower Gel Packaging Design

I need a new packaging design for a men shampoo and shower gel bottle. The packaging must me black (black bottle/package) and the logo should be also monochrom.
For example, black matte bottle and black shiny logo on the packaging (not mandatory).
the design must contain maximum 3 colors.
1. black
2. white (text)
3. grey/dark blue/dark green (colors will be the difference between products parfumes/smell/scences.

Design must be minimalist/elegant/discrete.
Updates

Please check the photos i added for pure inspiration.

Target Market(s)

brand exclusively for MEN - premium clients

Industry/Entity Type

Cosmetics

Font styles to use
Sans Serif

Colors
1b1b1b
5c5c5c
aaaaaa
ffffff
3176b5

Requirements
Must have
• black background
• minimalist design

```html
<!DOCTYPE html>
<html lang="en">
<head>
<meta charset="utf-8">
<title>Norda Men Care Shower Gel Range</title>
<link rel="stylesheet" href="https://fonts.googleapis.com/css2?family=Josefin+Sans:wght@300;400&family=Montserrat:wght@500;600&display=swap">
<style>
  :root {
    --page: #ffffff;
    --bottle: #2b2827;
    --bottle-edge: #1b1b1b;
    --cap: #c4c4c4;
    --cap-light: #dedede;
    --white: #ffffff;
    --script-tone: #5c5c5c;
    --amber: #d98a1f;
    --steel-blue: #3f77a3;
    --crimson: #b8323a;
  }
  * { box-sizing: border-box; margin: 0; padding: 0; }
  html, body { width: 1169px; height: 1200px; overflow: hidden; background: var(--page); }
  .range { position: relative; width: 1169px; height: 1200px; }
  .bottle { position: absolute; top: 125px; width: 219px; height: 810px; }
  .bottle--amber { left: 159px; --accent: var(--amber); }
  .bottle--blue { left: 499px; --accent: var(--steel-blue); }
  .bottle--crimson { left: 823px; --accent: var(--crimson); }
  .cap {
    position: absolute; left: 45px; top: 0; width: 128px; height: 133px;
    background: linear-gradient(90deg, var(--cap) 0%, var(--cap-light) 45%, var(--cap) 100%);
    border-radius: 6px 6px 2px 2px;
  }
  .body {
    position: absolute; left: 0; top: 129px; width: 219px; height: 681px;
    background: var(--bottle);
    border-radius: 30px 30px 6px 6px;
    border-bottom: 3px solid var(--bottle-edge);
  }
  .brand-mark {
    position: absolute; top: 108px; left: 101px;
    width: 17px; height: 17px; border-radius: 50%; background: var(--white);
  }
  .brand-name {
    position: absolute; top: 142px; width: 100%; text-align: center;
    font-family: "Josefin Sans", sans-serif; font-weight: 300;
    font-size: 22px; line-height: 26px; letter-spacing: 8px; color: var(--white); padding-left: 8px;
  }
  .brand-line {
    position: absolute; top: 169px; width: 100%; text-align: center;
    font-family: "Josefin Sans", sans-serif; font-weight: 300;
    font-size: 7px; line-height: 8px; letter-spacing: 3px; color: var(--script-tone);
  }
  .product {
    position: absolute; top: 275px; width: 100%; text-align: center;
    font-family: "Montserrat", sans-serif; font-weight: 600;
    font-size: 24px; line-height: 30px; color: var(--accent);
  }
  .tagline-art {
    position: absolute; top: 334px; left: 48px; width: 123px; height: 24px;
    background: var(--script-tone); border-radius: 3px;
  }
  .scent-band { position: absolute; left: 0; top: 428px; width: 219px; height: 130px; }
  .scent-band polygon { fill: var(--accent); }
  .volume {
    position: absolute; top: 610px; width: 100%; text-align: center;
    font-family: "Montserrat", sans-serif; font-weight: 600;
    font-size: 16px; line-height: 20px; color: var(--accent);
  }
</style>
</head>
<body>
<main class="range">
  <section class="bottle bottle--amber">
    <div class="cap"></div>
    <div class="body">
      <span class="brand-mark"></span>
      <div class="brand-name">NORDA</div>
      <div class="brand-line">cosmetics</div>
      <div class="product">SHOWER GEL</div>
      <div class="tagline-art" role="img" aria-label="Hand-lettered range tagline"></div>
      <svg class="scent-band" viewBox="0 0 219 130" role="img" aria-label="Diagonal colour band carrying the hand-lettered scent name"><polygon points="0,74 219,0 219,55 0,129"/></svg>
      <div class="volume">300ML</div>
    </div>
  </section>
  <section class="bottle bottle--blue">
    <div class="cap"></div>
    <div class="body">
      <span class="brand-mark"></span>
      <div class="brand-name">NORDA</div>
      <div class="brand-line">cosmetics</div>
      <div class="product">SHOWER GEL</div>
      <div class="tagline-art" role="img" aria-label="Hand-lettered range tagline"></div>
      <svg class="scent-band" viewBox="0 0 219 130" role="img" aria-label="Diagonal colour band carrying the hand-lettered scent name"><polygon points="0,74 219,0 219,55 0,129"/></svg>
      <div class="volume">300ML</div>
    </div>
  </section>
  <section class="bottle bottle--crimson">
    <div class="cap"></div>
    <div class="body">
      <span class="brand-mark"></span>
      <div class="brand-name">NORDA</div>
      <div class="brand-line">cosmetics</div>
      <div class="product">SHOWER GEL</div>
      <div class="tagline-art" role="img" aria-label="Hand-lettered range tagline"></div>
      <svg class="scent-band" viewBox="0 0 219 130" role="img" aria-label="Diagonal colour band carrying the hand-lettered scent name"><polygon points="0,74 219,0 219,55 0,129"/></svg>
      <div class="volume">300ML</div>
    </div>
  </section>
</main>
</body>
</html>
```